TotPlanet Community Landing Page

TotPlanet is a virtual world built with childrens' needs in mind. It is an online portal where parents will find all kids' related stuffs and a community connect point for parents to interact and share their experiences.

We need the designs for 2 pages within TotPlanet:
- Landing Page for the Community Area
- Registration page for membership

1) The Landing Page need to have the following:

Logo & Main Background :- use the images attached

Page Title & Navigation Menu :-
The page title is "Community Connect"; navigation menu should be able to hold at least 6 tabs

Login Widget* :-
We want to put emphasis on the design of this.
For visitors, this is a normal login widget with username/password input fields, register button and 'login with chatterbook' button.
For logged-in users, this becomes a simple dashboard widget with Avatar, shortlinks and some useful navigation buttons.

"Groups" Section :-
This area holds an image, a short paragraph introducing "Groups", a widget showing 5-10 latest/popular groups and a 'Go to Groups' button at the bottom.

"Forum" Section :-
This area holds an image, a short paragraph introducing "Forum", a widget showing 5-10 latest/popular discussion topics and a 'Go to Forum' button at the bottom.

"Activities" Section -
This area holds an image, a short paragraph introducing "Forum", a widget showing 5-10 latest/popular events & activities and a 'Go to Activities' button at the bottom.

"Marketplace" Section :-
This area holds an image, a short paragraph introducing "Marketplace", a widget showing 5-10 latest/popular products and a 'Go to Marketplace' button at the bottom.

Social Media elements :-
The usual social media icons and chatterbook like box.

2) The Registration Page will need to contain the registration form as per the image attached.

Target Market(s)

Parents with kids ranging from 2 - 12 years old

Industry/Entity Type

Events

Requirements
Nice to have
• - colorful illustrations of kids or kids related images all around

```html
<!DOCTYPE html>
<html lang="en">
<head>
<meta charset="utf-8">
<title>TotPlanet – Community Connect</title>
<link href="https://fonts.googleapis.com/css2?family=Alfa+Slab+One&family=Bubblegum+Sans&family=Kalam:wght@400;700&display=swap" rel="stylesheet">
<style>
:root{
  --sky-top:#3aa6d8;
  --sky-low:#bfe6f4;
  --grass:#6f9a2a;
  --grass-dark:#4d7417;
  --nav-green:#4cb83a;
  --nav-yellow:#ffe41a;
  --nav-text:#2f8a1f;
  --red:#e0101a;
  --red-dark:#c40010;
  --pink-field:#ffc6cc;
  --orange:#ff8a12;
  --orange-btn:#f57b0c;
  --cream:#fff0e2;
  --purple:#b13de6;
  --purple-dark:#9a1fd8;
  --blue:#1a9be0;
  --gold:#d9a326;
  --text-orange:#e8700a;
  --text-blue:#1fa3d6;
  --text-grey:#9a9a9a;
  --white:#ffffff;
}
*{box-sizing:border-box;margin:0;padding:0}
html,body{width:960px;height:1200px;overflow:hidden}
body{
  position:relative;
  font-family:Arial,Helvetica,sans-serif;
  background:linear-gradient(180deg,var(--sky-top) 0%,var(--sky-low) 38%,#9cc44a 48%,var(--grass) 58%,var(--grass-dark) 100%);
}
.scenery{position:absolute;left:0;top:0;width:960px;height:1200px}
.abs{position:absolute}

.page{position:absolute;left:104px;top:132px;width:750px;height:982px;background:var(--white);border-radius:12px}

.brand{left:128px;top:108px;font-family:'Bubblegum Sans',cursive;font-size:52px;color:var(--purple-dark);line-height:1}
.hill{left:300px;top:104px}
.page-title{left:360px;top:134px;width:240px;text-align:center;font-family:'Bubblegum Sans',cursive;font-size:40px;line-height:38px;color:#d9fff0;letter-spacing:1px}

.search{left:664px;top:149px;width:178px;height:27px;border-radius:8px;background:#fbefc2;font-family:'Kalam',cursive;color:#c7b27a;font-size:14px;padding:3px 12px}
.search-btn{position:absolute;right:4px;top:3px;width:27px;height:21px;border-radius:5px;background:#d8b757}
.social{top:189px;width:22px;height:22px;border-radius:50%;background:#1b8fd6}

.nav{left:94px;top:225px;width:770px;height:37px;background:linear-gradient(#59c745,#2f9a28);border-radius:3px}
.nav a{position:absolute;top:4px;height:26px;background:var(--nav-yellow);border-radius:5px;font-family:'Bubblegum Sans',cursive;font-size:17px;color:var(--nav-text);text-decoration:none;text-align:center;line-height:27px;letter-spacing:1px;box-shadow:0 2px 0 #c8a800}

.login{left:113px;top:271px;width:188px;height:218px;background:linear-gradient(var(--red),var(--red-dark));border-radius:12px;border:2px solid #f7d3d3}
.login h2{position:absolute;left:34px;top:18px;font-family:'Kalam',cursive;font-weight:400;font-size:26px;color:var(--white)}
.field{position:absolute;left:13px;width:161px;height:24px;border-radius:12px;background:var(--pink-field);font-family:'Kalam',cursive;font-size:12px;color:#c0101a;padding:3px 14px}
.pill{position:absolute;top:131px;height:25px;border-radius:12px;background:var(--orange-btn);border:2px solid #ffb56a;font-family:'Kalam',cursive;font-size:12px;color:var(--white);text-align:center;line-height:21px}
.register{position:absolute;left:21px;top:174px;font-family:'Kalam',cursive;font-size:12px;color:var(--white)}

.banner{left:314px;top:271px;width:332px;height:218px;border-radius:12px;background:linear-gradient(#8fd3f3,#b9e3f7 55%,#f7d24a 75%,#73b83a);}
.caption{left:322px;top:432px;width:318px;height:50px;border-radius:6px;background:linear-gradient(#2ea8e6,#1689cc);border:2px solid #9bd8f5;color:var(--white);font-family:'Alfa Slab One',serif;font-size:11px;line-height:14px;padding:9px 14px}
.play{left:589px;top:438px;width:38px;height:38px;border-radius:50%;background:var(--white)}

.quote{left:656px;top:271px;width:190px;height:218px;border-radius:12px;background:linear-gradient(var(--purple),var(--purple-dark));border:2px solid #e7c4f7;overflow:hidden}
.quote h2{position:absolute;left:24px;top:14px;font-family:'Kalam',cursive;font-weight:400;font-size:21px;color:var(--white)}
.quote p{position:absolute;left:20px;top:62px;width:166px;font-family:'Alfa Slab One',serif;font-size:16px;line-height:23px;color:var(--white)}
.quote-art{position:absolute;left:32px;top:152px;width:150px;height:70px;border-radius:40px 40px 0 0;background:linear-gradient(#ffc46b,#f0a640)}

.tab{top:510px;height:42px;border-radius:10px 10px 0 0;font-family:'Alfa Slab One',serif;font-size:22px;color:var(--white);text-align:center;line-height:46px}
.panel{left:111px;top:550px;width:735px;height:264px;background:var(--orange);border-radius:10px}
.groups-art{left:130px;top:564px;width:181px;height:146px;border-radius:12px;border:3px solid var(--white);background:linear-gradient(#d9f1fb,#e7f6fb 45%,#7cc23a 70%,#5aa82a)}
.groups-intro{left:134px;top:718px;width:180px;font-size:9.6px;line-height:11.6px;color:var(--white)}
.list{left:329px;top:563px;width:503px;height:239px;background:var(--cream);border-radius:10px}
.item{position:absolute;width:230px}
.item h3{font-size:11.5px;font-weight:bold;color:var(--text-orange)}
.go{display:inline-block;margin-top:5px;height:17px;padding:0 6px;background:var(--orange-btn);border-radius:2px;font-size:8.5px;font-weight:bold;color:var(--white);line-height:17px}
.rule{position:absolute;left:17px;width:470px;border-top:1px dotted #d9a980}

.testimonials{left:111px;top:834px;width:357px;height:265px;border:1px solid #f7e2c8;border-radius:10px;background:var(--white)}
.testimonials h2{position:absolute;left:20px;top:10px;font-family:'Alfa Slab One',serif;font-weight:400;font-size:23px;color:var(--text-orange);letter-spacing:1px}
.t-art{position:absolute;border-radius:10px;background:linear-gradient(#d9eef7,#f3d7a9)}
.t-text{position:absolute;left:174px;width:178px}
.t-text h3{font-size:14px;font-weight:normal;color:var(--text-blue);line-height:16px}
.t-text p{margin-top:3px;font-size:9px;line-height:14px;color:var(--text-grey)}
.t-text b{color:var(--text-orange)}
.t-rule{position:absolute;left:18px;top:155px;width:330px;border-top:1px dotted #f0d18a}

.famous{left:484px;top:834px;width:358px;height:265px;border-radius:10px;background:linear-gradient(var(--gold),#c99430)}
.famous h2{position:absolute;left:0;top:16px;width:358px;text-align:center;font-family:'Alfa Slab One',serif;font-weight:400;font-size:23px;color:var(--white);letter-spacing:1px}
.famous-art{position:absolute;left:61px;top:56px;width:237px;height:158px;border-radius:12px;border:3px solid var(--white);background:linear-gradient(160deg,#eaf7fd,#a9dcf3)}
.arrow{position:absolute;top:114px;width:42px;height:42px}
.famous .label{position:absolute;left:0;top:222px;width:358px;text-align:center;font-family:'Kalam',cursive;font-size:21px;color:var(--white)}

.footer-brand{left:380px;top:1124px;width:200px;text-align:center;font-family:'Bubblegum Sans',cursive;font-size:30px;color:#e9f2d2}
.copyright{left:280px;top:1181px;width:400px;text-align:center;font-size:8px;color:var(--white)}
</style>
</head>
<body>

<svg class="scenery" viewBox="0 0 960 1200" role="img" aria-label="Sky with rainbow, clouds and rolling green hills">
  <path d="M0 520 Q200 470 480 520 T960 500 V1200 H0Z" fill="#7da835" opacity=".6"/>
  <path d="M0 620 Q300 560 620 610 T960 580 V1200 H0Z" fill="#5f8d22" opacity=".5"/>
</svg>

<div class="page"></div>

<svg class="abs hill" width="420" height="130" viewBox="0 0 420 130" aria-hidden="true">
  <path d="M40 120 C80 10 300 -10 410 120Z" fill="#7cc51e"/>
</svg>

<div class="abs brand">TotPlanet</div>
<h1 class="abs page-title">Community Connect</h1>

<div class="abs search">search<span class="search-btn"></span></div>
<span class="abs social" style="left:703px" aria-label="Social link 1"></span>
<span class="abs social" style="left:732px" aria-label="Social link 2"></span>
<span class="abs social" style="left:762px" aria-label="Social link 3"></span>
<span class="abs social" style="left:791px" aria-label="Social link 4"></span>
<span class="abs social" style="left:820px" aria-label="Social link 5"></span>

<nav class="abs nav">
  <a style="left:26px;width:68px">HOME</a>
  <a style="left:112px;width:104px">ABOUT US</a>
  <a style="left:234px;width:64px">BLOG</a>
  <a style="left:316px;width:136px">TESTIMONIALS</a>
  <a style="left:466px;width:134px">MY ACCOUNT</a>
  <a style="left:614px;width:122px">CONTACT US</a>
</nav>

<section class="abs login">
  <h2>My Login</h2>
  <div class="field" style="top:66px">username</div>
  <div class="field" style="top:98px">password</div>
  <div class="pill" style="left:17px;width:46px">login</div>
  <div class="pill" style="left:73px;width:100px">chatterbook login</div>
  <div class="register">Register Here!</div>
</section>

<div class="abs banner" role="img" aria-label="Illustration of happy children jumping on a sunny hill"></div>
<div class="abs caption">World with full of fun, groups,<br>and activities only at TotPlanet</div>
<svg class="abs play" viewBox="0 0 38 38" aria-hidden="true"><polygon points="15,11 28,19 15,27" fill="#1a9be0"/></svg>

<section class="abs quote">
  <h2>Today’s Quote</h2>
  <p>“You can't win unless you know how to lose”</p>
  <div class="quote-art" role="img" aria-label="Illustration of a cheerful child"></div>
</section>

<div class="abs tab" style="left:154px;width:120px;background:var(--orange)">Groups</div>
<div class="abs tab" style="left:277px;width:113px;background:var(--purple)">Forum</div>
<div class="abs tab" style="left:393px;width:129px;background:var(--blue)">Activies</div>
<div class="abs tab" style="left:525px;width:189px;background:var(--red)">Market Place</div>

<div class="abs panel"></div>
<div class="abs groups-art" role="img" aria-label="Illustration of children peeking over grass"></div>
<p class="abs groups-intro">Lorem ipsum dolor sit amet, consectetur adipisicing elit, sed do eiusmod tempor incididunt ut labore et dolore magna aliqua. Ut enim ad minim veniam, quis nostrud exercitation ullamco laboris nisi ut aliquip ex ea commodo consequat.</p>

<div class="abs list">
  <div class="item" style="left:17px;top:16px"><h3>Lorem ipsum dolor sit amet</h3><span class="go">Go to Groups</span></div>
  <div class="item" style="left:265px;top:16px"><h3>Ut enim ad minim veniam, quis nostrud</h3><span class="go">Go to Groups</span></div>
  <div class="rule" style="top:63px"></div>
  <div class="item" style="left:17px;top:72px"><h3>Consectetur adipisicing elit, sed</h3><span class="go">Go to Groups</span></div>
  <div class="item" style="left:265px;top:72px"><h3>Exercitation ullamco laboris nisi ut</h3><span class="go">Go to Groups</span></div>
  <div class="rule" style="top:119px"></div>
  <div class="item" style="left:17px;top:128px"><h3>Do eiusmod tempor incididunt</h3><span class="go">Go to Groups</span></div>
  <div class="item" style="left:265px;top:128px"><h3>Aliquip ex ea commodo consequat</h3><span class="go">Go to Groups</span></div>
  <div class="rule" style="top:175px"></div>
  <div class="item" style="left:17px;top:184px"><h3>Ut labore et dolore magna aliqua</h3><span class="go">Go to Groups</span></div>
  <div class="item" style="left:265px;top:184px"><h3>Duis aute irure dolor in reprehenderit in</h3><span class="go">Go to Groups</span></div>
</div>

<section class="abs testimonials">
  <h2>OUR TESTIMONIALS</h2>
  <div class="t-art" style="left:20px;top:46px;width:140px;height:100px" role="img" aria-label="Illustration of a family together"></div>
  <div class="t-text" style="top:56px">
    <h3>Lorem ipsum dolor sit amet, consectetur adipisicing</h3>
    <p>Lorem ipsum dolor sit amet, consectetur adipisicing elit, sed do eiusmod tempor incididunt ut&nbsp;&nbsp;<b>more ›</b></p>
  </div>
  <div class="t-rule"></div>
  <div class="t-art" style="left:17px;top:170px;width:140px;height:80px" role="img" aria-label="Illustration of a mother and child"></div>
  <div class="t-text" style="top:179px">
    <h3>Ipsum dolor sit amet, set consectetur</h3>
    <p>Lorem ipsum dolor sit amet, consectetur adipisicing elit, sed do eiusmod tempor incididunt ut&nbsp;&nbsp;<b>more ›</b></p>
  </div>
</section>

<section class="abs famous">
  <h2>FAMOUS ACTIVITIES</h2>
  <div class="famous-art" role="img" aria-label="Illustration of children flying a kite"></div>
  <svg class="arrow" style="left:9px" viewBox="0 0 42 42" aria-label="Previous"><circle cx="21" cy="21" r="20" fill="#fff"/><polygon points="25,12 13,21 25,30" fill="#c99430"/></svg>
  <svg class="arrow" style="left:307px" viewBox="0 0 42 42" aria-label="Next"><circle cx="21" cy="21" r="20" fill="#fff"/><polygon points="17,12 29,21 17,30" fill="#c99430"/></svg>
  <div class="label">playing kite</div>
</section>

<div class="abs footer-brand">TotPlanet</div>
<div class="abs copyright">© Copyright 2013 TotPlanet. All Rights Reserved</div>

</body>
</html>
```